CODED website - Breakfree418

I am a successful entrepreneur - have recently sold my business and am semi-retired. I want to give something back, as well as provide a blog for articles and my journeys.

I will also be using this to provide free business and entrepreneurial advice.

I am creating a NOT FOR PROFIT business called Breakfree418.com.au which will provide the following;

1. Blog and articles; my travels, Small to Medium business advice and articles

2. My Bucket List - the 100 things I aim to achieve

3. Free business / start up advice - a section on the website which provides case studies on people / businesses which ask me for advice. We will then chronicle their story and what advice we have given for them to succeed.

My inspiration is the Martin Okonkwo idea and website;

http://martinokonkwo.example/about-martin/

Obviously I do NOT want a copy of this site, but use this for inspiration.

Furthermore, I would be interested in ongoing collaboration with the successful designer - I will be providing advice and consultancy to start ups, all of which will need web design etc, so there is ongoing referral streams for the successful designer.

I need this to be CODED and then uplifted to the website, so please DO NOT bid on this unless you can provide a coded site and facilitate the upload to WildHostings.

The NECESSARY tabs / pages

Main landing page - a short introduction into the ethos of Breakfree418

Writing - this will be the blog articles

About

Our Bucket List - a section where we can add our 100 buket list items. Hyperlinked to open a new page which has details on each bucket list item (ie #1 Make Breakfree418 - hyperlink to a new page which then has info on the bucklist item and what we have done)

Breakfree418 - this will be the section where we discuss people / businesses that we are helping. We will have an opening intro section + a link to the contact us page so they can ask us for the free advice. This will be the section where we have case studies into businesses / people that we have helped.
Updates

Hey everyone!

I'm really keen to get this website launched and looking amazing - if you have any questions, or would like to discuss anything at all, please email me at

dave@pinnaclepost.example.au

As I mentioned in the brief, I am doing this site to give back; I will not be earning a cent, and I will not be trying to earn any funds. I'm doing it simply to help other start ups or entrepreneurs, so I really want this site to look amazing.

I hope someone reads this and is inspired, and wants to be involved in this social enterprise with me.

Really excited to hear from you all and see your designs!

Industry/Entity Type

Business

Requirements
Must have
• MUST BE CODED and uplifted to the WildHosting registered domain - www.breakfree418.com.au - happy to discuss additional costings for this with successful designer.

Separate pages for each section (as outlined in the brief above)

Blog section to look similar to http://martinokonkwo.example/3x5/

Comprehensive website - not a simple wordpress template theme with some minor modifications. I will immediately reject any simple template design. I am looking for a slick, fully functioning website design.

PLEASE BE AWARE that I am looking for ongoing collaboration with the www.breakfree418.com.au.

I am trying this website as I want to find a young, energetic, vibrant, dynamic designer - this is your opportunity to be a part of something big, as this website will be huge!

Please do not submit a design if you are not motivated and ready for something big.

```html
<!DOCTYPE html>
<html lang="en">
<head>
<meta charset="utf-8">
<title>Breakfree 418</title>
<link rel="stylesheet" href="https://fonts.googleapis.com/css2?family=Bitter:wght@400;500;600&family=Barlow:wght@500;600&display=swap">
<style>
:root{
  --sky:#5aa9ab;
  --sky-light:#cfe6df;
  --sand:#e9e1c2;
  --sand-deep:#d8cd98;
  --paper:#fdfdfb;
  --ink-dark:#0d4a4a;
  --teal:#1a8585;
  --tab:#7cb2b4;
  --tab-line:#e6f2f1;
  --text:#333333;
  --rule:#d8d3b4;
  --hero-bg:#e9dcbd;
  --hero-frame:#f5efe0;
  --search-btn:#c9bf86;
  --chirp:#5ec2e6;
  --friend:#1366ae;
  --pinboard:#cb2027;
}
*{margin:0;padding:0;box-sizing:border-box}
html,body{width:1200px;height:900px;overflow:hidden}
body{
  position:relative;
  font-family:Arial,Helvetica,sans-serif;
  background:linear-gradient(180deg,var(--sky) 0,var(--sky-light) 60px,#f3efdc 140px,var(--sand) 420px,var(--sand) 100%);
}
.logo{
  position:absolute;top:48px;left:0;width:1200px;text-align:center;
  font-family:Bitter,serif;font-weight:500;font-size:58px;letter-spacing:12px;
  color:var(--ink-dark);line-height:1;
}
.main-nav{position:absolute;top:127px;left:125px;display:flex;gap:3px}
.main-nav a{
  width:188px;height:35px;background:var(--tab);color:#fff;text-decoration:none;
  font-family:Barlow,sans-serif;font-weight:500;font-size:16px;letter-spacing:.5px;
  display:flex;align-items:center;justify-content:center;position:relative;
}
.main-nav a::after{content:"";position:absolute;inset:3px 0;border-top:1px dashed var(--tab-line);border-bottom:1px dashed var(--tab-line)}
.main-nav a:last-child{justify-content:flex-end;padding-right:38px}
.frame{position:absolute;top:173px;left:125px;width:952px;height:740px;background:var(--sand-deep)}
.content{position:absolute;top:184px;left:137px;width:648px;height:720px;background:var(--paper)}
.sidebar{position:absolute;top:184px;left:789px;width:276px;height:720px;background:var(--paper)}
.post-title{position:absolute;top:218px;left:165px;font-family:Bitter,serif;font-weight:400;font-size:32px;color:var(--ink-dark);letter-spacing:.3px}
.title-rule{position:absolute;top:275px;left:157px;width:620px;border-top:2px dashed var(--rule)}
.hero{position:absolute;top:300px;left:163px;width:606px;height:212px;background:var(--hero-frame);box-shadow:0 1px 3px rgba(0,0,0,.08)}
.hero-photo{position:absolute;top:10px;left:8px;width:229px;height:192px;background:linear-gradient(135deg,#c9d3d8,#6f8fb5 55%,#b89c7c)}
.hero-panel{position:absolute;top:10px;left:237px;width:361px;height:192px;background:var(--hero-bg)}
.hero-heading{position:absolute;top:22px;left:26px;font-family:Bitter,serif;font-size:39px;line-height:48px;color:var(--ink-dark);letter-spacing:1px}
.hero-rule{position:absolute;top:127px;left:25px;width:306px;height:12px}
.hero-since{position:absolute;top:142px;right:34px;font-family:Bitter,serif;color:var(--ink-dark);font-size:24px;letter-spacing:1px}
.hero-since b{font-weight:400;font-size:36px}
.article{position:absolute;top:536px;left:164px;width:606px;font-size:12.5px;line-height:18px;color:var(--text)}
.article p{margin-bottom:18px}
.article .lead{color:var(--teal);font-weight:bold}
.article a{color:var(--teal)}
.article h2{font-family:Bitter,serif;font-weight:500;font-size:19px;color:var(--teal);margin:34px 0 16px}
.search{position:absolute;top:203px;left:801px;width:252px;height:35px;display:flex;border:1px solid #d0d0d0;background:#fff}
.search span{flex:1;padding:9px 10px;font-size:15px;color:#aaa}
.search i{width:44px;background:var(--search-btn);display:flex;align-items:center;justify-content:center}
.widget-title{
  position:absolute;left:789px;width:276px;height:35px;background:var(--tab);color:#fff;
  font-family:Barlow,sans-serif;font-weight:500;font-size:18px;letter-spacing:.5px;padding:7px 0 0 15px;
}
.widget-title::after{content:"";position:absolute;inset:3px 0;border-top:1px dashed var(--tab-line);border-bottom:1px dashed var(--tab-line)}
.categories{position:absolute;top:298px;left:799px;width:244px;list-style:none}
.categories li{height:32px;border-bottom:1px solid var(--rule);display:flex;align-items:center;font-size:12px;color:var(--teal)}
.categories li:last-child{border-bottom:0}
.categories svg{margin:0 12px 0 6px}
.social{position:absolute;left:805px;width:243px;height:34px;color:#fff;display:flex;align-items:center;justify-content:space-between;padding:0 12px 0 15px;font-family:Barlow,sans-serif;font-weight:600;font-size:13px;letter-spacing:.6px}
.social strong{font-family:Barlow,sans-serif;font-weight:600;font-size:19px;letter-spacing:0;display:flex;align-items:center;gap:6px}
.social strong i{width:14px;height:14px;background:rgba(255,255,255,.85);display:inline-block}
.chirp{top:559px;background:var(--chirp)}
.friend{top:607px;background:var(--friend)}
.pinboard{top:656px;background:var(--pinboard)}
.recent{position:absolute;left:801px;width:244px;display:flex;gap:10px;padding-bottom:12px;border-bottom:1px dashed #bbb}
.recent .thumb{width:42px;height:42px;flex:none;border:2px solid #fff;box-shadow:0 0 0 1px #ccc;background:linear-gradient(160deg,#6c8aa8,#2f4b66)}
.recent h3{font-family:Bitter,serif;font-weight:400;font-size:13.5px;line-height:16px;color:var(--teal);margin-top:-2px}
.recent small{font-family:Barlow,sans-serif;font-size:11.5px;color:#888;letter-spacing:.3px}
</style>
</head>
<body>
<div class="logo">BREAKFREE 418</div>

<nav class="main-nav">
  <a href="#">ABOUT US</a><a href="#">PLACE</a><a href="#">WRITING</a><a href="#">STORE</a><a href="#">CONTACT US</a>
</nav>

<div class="frame"></div>
<main class="content"></main>
<aside class="sidebar"></aside>

<h1 class="post-title">Lorem ipsum is simply dummy text</h1>
<div class="title-rule"></div>

<section class="hero">
  <div class="hero-photo" role="img" aria-label="Photo of an older man painting with watercolours at a table"></div>
  <div class="hero-panel">
    <p class="hero-heading">Lorem ipsum is<br>simply dummy</p>
    <svg class="hero-rule" viewBox="0 0 306 12"><line x1="0" y1="6" x2="115" y2="6" stroke="#7a9d9a"/><line x1="191" y1="6" x2="306" y2="6" stroke="#7a9d9a"/></svg>
    <p class="hero-since">Since <b>1979</b></p>
  </div>
</section>

<article class="article">
  <p class="lead">Lorem Ipsum Text. Lorem ipsum dolor sit amet, consectetuer adipiscing elit. Nam cursus. Morbi ut mi. dfdff Nullam enim leo, egestas id, condimentum at, laoreet. Lorem Ipsum Text.</p>
  <p>Lorem ipsum dolor sit amet, consectetuer adipiscing elit. Nam cursus. Morbi ut mi. Nullam enim leo, eges tas id, condimentum at, laoreet. Lorem Ipsum Text. Lorem ipsum dolor sit amet, &nbsp;egestas consectetuer adipiscing elit. Nam cursus. Morbi ut mi. Nullam enim leo, egestas id, &nbsp;egestas condimentum at, laoreet. Lorem Ipsum Text. Lorem Ipsum Text. Lorem ipsum dolor sit amet, consectetuer adipiscing elit. Nam cursus. Morbi ut mi. Nullam enim leo, egestas id, condimentum at, laoreet. Lorem Ipsum Text.</p>
  <p>Lorem <a href="#">ipsum dolor sit amet, consectetuer adipiscing elit</a>. Nam cursus. Morbi ut mi. Nullam enim &nbsp;leo, egestas id, condimentum at, laoreet. Lorem Ipsum Text. Lorem ipsum dolor sit amet, consectetuer adipisc ing elit. Nam cursus. Morbi ut mi. Nullam enim leo, egestas id, condimentum at, laoreet.</p>
  <h2>Loren ipsum is simply</h2>
  <p>&nbsp;Lorem ipsum dolor sit amet, consectetuer adipiscing elit. Nam cursus. Morbi ut mi. Nullam enim leo, eges tas id, condimentum at, laoreet. Lorem Ipsum Text. Lorem ipsum dolor sit amet, &nbsp;egestas consectetuer adipiscing elit. Nam cursus. Morbi ut mi. Nullam enim leo, egestas id, &nbsp;egestas condimentum at, laoreet. Lorem Ipsum Text. Lorem Ipsum Text. Lorem ipsum dolor sit amet, consectetuer adipiscing elit. Nam cursus. Morbi ut mi. Nullam enim leo, egestas id, condimentum at, laoreet. Lorem Ipsum Text.</p>
</article>

<div class="search">
  <span>Search here</span>
  <i><svg width="24" height="22" viewBox="0 0 24 22"><circle cx="9" cy="9" r="6" fill="none" stroke="#fff" stroke-width="2.5"/><line x1="13.5" y1="13" x2="21" y2="19" stroke="#fff" stroke-width="3.5" stroke-linecap="round"/></svg></i>
</div>

<div class="widget-title" style="top:253px">CATEGORIES</div>
<ul class="categories">
  <li><svg width="13" height="13" viewBox="0 0 13 13"><path d="M6.5 0v13M0 6.5h13" stroke="#4a8c8c"/><path d="M6.5 0l-2 2h4zM6.5 13l-2-2h4zM0 6.5l2-2v4zM13 6.5l-2-2v4z" fill="#4a8c8c"/></svg>Ipsum Text &nbsp;Lorem ipsum lorem dumm</li>
  <li><svg width="13" height="13" viewBox="0 0 13 13"><path d="M6.5 0v13M0 6.5h13" stroke="#4a8c8c"/><path d="M6.5 0l-2 2h4zM6.5 13l-2-2h4zM0 6.5l2-2v4zM13 6.5l-2-2v4z" fill="#4a8c8c"/></svg>Lorem Ipsum Text &nbsp;Lorem ipsum here</li>
  <li><svg width="13" height="13" viewBox="0 0 13 13"><path d="M6.5 0v13M0 6.5h13" stroke="#4a8c8c"/><path d="M6.5 0l-2 2h4zM6.5 13l-2-2h4zM0 6.5l2-2v4zM13 6.5l-2-2v4z" fill="#4a8c8c"/></svg>Dummy Text &nbsp;Lorem ipsum lorem</li>
  <li><svg width="13" height="13" viewBox="0 0 13 13"><path d="M6.5 0v13M0 6.5h13" stroke="#4a8c8c"/><path d="M6.5 0l-2 2h4zM6.5 13l-2-2h4zM0 6.5l2-2v4zM13 6.5l-2-2v4z" fill="#4a8c8c"/></svg>Ipsum Text &nbsp;Lorem ipsum lorem dumm</li>
  <li><svg width="13" height="13" viewBox="0 0 13 13"><path d="M6.5 0v13M0 6.5h13" stroke="#4a8c8c"/><path d="M6.5 0l-2 2h4zM6.5 13l-2-2h4zM0 6.5l2-2v4zM13 6.5l-2-2v4z" fill="#4a8c8c"/></svg>Lorem Ipsum Text &nbsp;Lorem ipsum here</li>
  <li><svg width="13" height="13" viewBox="0 0 13 13"><path d="M6.5 0v13M0 6.5h13" stroke="#4a8c8c"/><path d="M6.5 0l-2 2h4zM6.5 13l-2-2h4zM0 6.5l2-2v4zM13 6.5l-2-2v4z" fill="#4a8c8c"/></svg>Lorem Ipsum Text &nbsp;Lorem ipsum</li>
</ul>

<div class="widget-title" style="top:507px">CONNECT WITH US</div>
<a class="social chirp" href="#">FOLLOW US ON <strong>Chirpline <i></i></strong></a>
<a class="social friend" href="#">JOIN US ON <strong>Friendbook <i></i></strong></a>
<a class="social pinboard" href="#">PIN US ON <strong>Pinboardly <i></i></strong></a>

<div class="widget-title" style="top:718px">RECENT POST</div>
<div class="recent" style="top:770px">
  <div class="thumb" role="img" aria-label="Author portrait"></div>
  <div><h3>Lorem ipsum all time favorite personal finance book!</h3><small>Jan 03, 2013. by admin</small></div>
</div>
<div class="recent" style="top:841px">
  <div class="thumb" role="img" aria-label="Author portrait"></div>
  <div><h3>Lorem ipsum all time favorite personal finance book!</h3><small>Jan 03, 2013. by admin</small></div>
</div>
</body>
</html>
```